Orbit 582 - Kindle Book Cover

I am looking for a Kindle book cover for my book about "Orbit 582".
The Book is Titled:
Orbit 582 Ascended
Shaping Tomorrow: Paths To Unlocking Hidden Currents
Author is Dorian Welby
Here is a book description that may help you understand more about it:
Inspired by the genius of Bertram Ollinger, this comprehensive guide delves into the ancient wisdom and cutting-edge science behind the 582 method, a powerful tool for manifesting your desires. Whether you're seeking personal growth, financial success, or spiritual enlightenment, this book provides advanced techniques and methods to transform your dreams into reality.
Any questions please ask.
Thanks
Gavin

```html
<!DOCTYPE html>
<html lang="en">
<head>
<meta charset="utf-8">
<title>Orbit 582 – Book Cover</title>
<link rel="stylesheet" href="https://fonts.googleapis.com/css2?family=Cormorant+Garamond:wght@300;400;500&family=Marcellus&display=swap">
<style>
  :root {
    --backdrop: #d6d6d6;
    --gold: #dcaa6c;
    --gold-soft: #c99a62;
    --glow-core: #f4dcc0;
    --glow-warm: #b97d52;
    --ember: #7a4a3a;
    --dusk: #3d2c36;
    --night: #241b26;
  }
  html, body {
    margin: 0;
    padding: 0;
    width: 1200px;
    height: 1200px;
    overflow: hidden;
    background: var(--backdrop);
  }
  .cover {
    position: absolute;
    left: 258px;
    top: 54px;
    width: 684px;
    height: 1092px;
    overflow: hidden;
    background: var(--night);
  }
  .cover-artwork {
    position: absolute;
    inset: 0;
    background:
      radial-gradient(ellipse 38% 30% at 50% 34%, var(--glow-core) 0%, rgba(230,180,130,0.7) 25%, rgba(185,125,82,0.35) 60%, rgba(185,125,82,0) 100%),
      radial-gradient(ellipse 75% 60% at 50% 40%, var(--glow-warm) 0%, var(--ember) 45%, var(--dusk) 80%, var(--night) 100%);
  }
  .cover-text {
    position: absolute;
    left: 0;
    width: 100%;
    text-align: center;
    color: var(--gold);
    margin: 0;
  }
  .subtitle {
    top: 36px;
    font-family: "Cormorant Garamond", serif;
    font-weight: 500;
    font-size: 14px;
    line-height: 21px;
    letter-spacing: 0.4px;
    color: var(--gold-soft);
    text-transform: uppercase;
  }
  .title-word {
    top: 300px;
    font-family: "Cormorant Garamond", serif;
    font-weight: 400;
    font-size: 78px;
    line-height: 1;
    letter-spacing: 9px;
    text-transform: uppercase;
  }
  .title-number {
    top: 376px;
    font-family: "Cormorant Garamond", serif;
    font-weight: 300;
    font-size: 150px;
    line-height: 1;
  }
  .author {
    top: 945px;
    font-family: "Marcellus", serif;
    font-size: 40px;
    line-height: 1;
    letter-spacing: 4px;
    text-transform: uppercase;
  }
</style>
</head>
<body>
  <main class="cover">
    <div class="cover-artwork" role="img" aria-label="Cosmic illustration: a figure meditating cross-legged on a stone platform, facing a glowing portal of concentric golden rings with a luminous standing figure at its centre"></div>
    <p class="cover-text subtitle">Shaping Tomorrow<br>Paths To Unlocking Hidden Currents</p>
    <h1 class="cover-text title-word">Orbit</h1>
    <p class="cover-text title-number">582</p>
    <p class="cover-text author">Dorian Welby</p>
  </main>
</body>
</html>
```